business card for author of crime novel

I am an author with a new book. I need a business card with the book's cover on one side (already uploaded), and contact details on the other.

Walt Pemberty
Author

telephone: 646-512-7380
website: www.waltpemberty.net
facebook: pagehall.net/wpemberty
twitter: chirpline.net/wpemberty
email: wpemberty@postvale.net

Target Market(s)

Readers of mystery books

Industry/Entity Type

Business

Contact Information for Business Card

Walt Pemberty
Author

telephone: 646-512-7380

Font styles to use
Serif
Sans Serif

Requirements
Must have
• Book cover on one side. My contact info on the other, with the name of the book repeated if that makes sense. Clean design.
Should not have
• Overly ornate, too formal, too distracting

```html
<!DOCTYPE html>
<html lang="en">
<head>
<meta charset="utf-8">
<title>Walt Pemberty – Author Business Card</title>
<link href="https://fonts.googleapis.com/css2?family=Cinzel:wght@600;700&family=Crimson+Text:wght@400&family=Lato:wght@400&display=swap" rel="stylesheet">
<style>
  :root {
    --page: #ececec;
    --ink-black: #0b0b0b;
    --stone-dark: #2a2725;
    --stone-mid: #5e5955;
    --stone-light: #8d8780;
    --cover-gold: #d9a12a;
    --cover-blue: #7f98a3;
    --paper-white: #f4f4f2;
    --card-shadow: rgba(0, 0, 0, 0.28);
  }
  * { box-sizing: border-box; margin: 0; padding: 0; }
  html, body {
    width: 1200px;
    height: 800px;
    overflow: hidden;
    background: var(--page);
  }
  .canvas {
    position: relative;
    width: 1200px;
    height: 800px;
    display: flex;
    align-items: center;
    justify-content: center;
    gap: 40px;
  }
  .card {
    position: relative;
    width: 525px;
    height: 300px;
    overflow: hidden;
    box-shadow: 0 6px 18px var(--card-shadow);
  }

  /* Contact side */
  .card--contact {
    background:
      radial-gradient(ellipse at 70% 35%, var(--stone-light) 0%, var(--stone-mid) 35%, var(--stone-dark) 70%, var(--ink-black) 100%);
  }
  .wall-texture {
    position: absolute;
    inset: 0;
    background: linear-gradient(200deg, rgba(140,134,128,0.35) 0%, rgba(60,56,53,0.2) 45%, rgba(0,0,0,0.75) 100%);
  }
  .book-cover {
    position: absolute;
    left: 250px;
    top: 40px;
    width: 215px;
    height: 150px;
    border-radius: 3px;
    background: linear-gradient(135deg, var(--cover-gold) 0%, #c98f1e 100%);
    box-shadow: 4px 8px 12px rgba(0,0,0,0.5);
  }
  .book-cover__art {
    position: absolute;
    inset: 12px 14px 34px 14px;
    background: linear-gradient(160deg, #a9bcc4 0%, var(--cover-blue) 50%, #3f5158 100%);
  }
  .contact-block {
    position: absolute;
    left: 28px;
    bottom: 26px;
    color: var(--paper-white);
  }
  .contact-block__name,
  .contact-block__role {
    font-family: "Crimson Text", serif;
    font-size: 19px;
    line-height: 1.1;
  }
  .contact-block__role { margin-bottom: 8px; }
  .contact-block__list {
    list-style: none;
    font-family: "Lato", sans-serif;
    font-size: 11.5px;
    line-height: 1.35;
    padding-left: 10px;
  }

  /* Name side */
  .card--name {
    background:
      linear-gradient(115deg, var(--ink-black) 0%, #141312 30%, var(--stone-dark) 60%, var(--stone-mid) 85%, var(--stone-light) 100%);
  }
  .quill-mark {
    position: absolute;
    right: 40px;
    top: 40px;
    width: 110px;
    height: 110px;
    border-radius: 6px;
    background: radial-gradient(circle, rgba(244,244,242,0.55) 0%, rgba(244,244,242,0.15) 65%, transparent 100%);
  }
  .author-name {
    position: absolute;
    left: 60px;
    bottom: 50px;
    color: var(--paper-white);
    font-family: "Cinzel", serif;
    font-weight: 700;
    text-shadow: 0 2px 6px rgba(0,0,0,0.6);
  }
  .author-name__first {
    display: block;
    font-size: 30px;
    margin-left: 70px;
    line-height: 1;
    margin-bottom: 10px;
  }
  .author-name__last {
    display: block;
    font-size: 52px;
    letter-spacing: 1px;
    line-height: 1;
  }
</style>
</head>
<body>
<main class="canvas">
  <section class="card card--contact">
    <div class="wall-texture" role="img" aria-label="Weathered dark stone wall texture"></div>
    <div class="book-cover" role="img" aria-label="Book cover of Dead Drop Alley, A Marlow Greer Mystery by Pemberty, a gold cover framing a city building at night">
      <div class="book-cover__art"></div>
    </div>
    <div class="contact-block">
      <p class="contact-block__name">Walt Pemberty</p>
      <p class="contact-block__role">Author</p>
      <ul class="contact-block__list">
        <li>646-512-7380</li>
        <li>www.waltpemberty.net</li>
        <li>pagehall.net/wpemberty</li>
        <li>chirpline.net/wpemberty</li>
        <li>wpemberty@postvale.net</li>
      </ul>
    </div>
  </section>

  <section class="card card--name">
    <div class="quill-mark" role="img" aria-label="White quill pen and inkwell illustration"></div>
    <h1 class="author-name">
      <span class="author-name__first">WALT</span>
      <span class="author-name__last">PEMBERTY</span>
    </h1>
  </section>
</main>
</body>
</html>
```